Specialist Medical practice after professional trifold flyer design for patient information brochure

I am the Director of the Hollowbrook Clinic, a specialist medial and surgical practice in Australia. I am after a professional design of a patient information trifold flyer that can be used for web distribution or for commercial printing for upcoming educational event. The design would need to allow change of images and text to be used as template for future topics but have a common brand look across them. Colours would follow the logo, but primarily blue colours for the hollowbrook theme. The inside text needs to be clearly contrasted to the background for easy reading, as often elderly patients. The design would make use of curves or circles, but open for hexagonal, triangle square vector components. I have included an outline for the initial brochure and included images to include. Other stock background images can be used if they increase the impact of the design over included. A winning design is also one that could be modified to a 4 page bi-fold brochure

Target Market(s)

This will be provided to patients in GP practices, podiatry clinics, radiological practices. Aimed at patients to read and be compelled to look to site or get consultation with me

Industry/Entity Type

Medical

Font styles to use
Serif
Sans Serif

Colors
33a6d7
0355a3
86cfc6
cedeed
0292cd
85cae6

Requirements
Must have
• The front cover needs to engage the patient to pick up and read- yes I have a painful ankle and want to find out more. the goal for the inside is to provide the options but be able to direct to website for more info - website currently undergoing upgrade. After professional modern look. Not bright contrasting colours like many advertising brochures. Needs to able to have images and text changed but following same look to create new topics
Nice to have
• The focus is a Tri-fold brochure. Nice to be able to modify to bifold. A winning design would even offer both, or submit separate bifold and trifold. I am open to different versions of similar look. (eg option of brochure with curved elements, triangular or square, or hexagonal.
Should not have
• To many contrasting colours. Text must be easily read on background, either white or coloured background texture with transparency

```html
<!DOCTYPE html>
<html lang="en">
<head>
<meta charset="utf-8">
<title>Hollowbrook Clinic – My Painful Ankle brochure</title>
<link rel="stylesheet" href="https://fonts.googleapis.com/css2?family=Open+Sans:ital,wght@0,400;0,600;0,700;1,700&family=PT+Sans:wght@400;700&display=swap">
<style>
:root{
  --navy:#0355a3;
  --deep:#0a3f8f;
  --bright:#0292cd;
  --sky:#33a6d7;
  --mist:#cedeed;
  --ink:#2a2a2a;
  --frame:#333333;
  --white:#ffffff;
}
*{margin:0;padding:0;box-sizing:border-box}
html,body{width:770px;height:1200px;overflow:hidden;background:var(--frame)}
body{position:relative;font-family:"PT Sans",Arial,sans-serif;color:var(--ink)}
.panel{position:absolute;overflow:hidden;background:var(--white)}
.panel > svg.bg{position:absolute;left:0;top:0}
.abs{position:absolute}
.photo{position:absolute}

/* outside */
.about{left:10px;top:11px;width:248px;height:580px}
.name-bar{left:22px;top:24px;width:212px;height:22px;background:var(--navy);color:var(--white);font:700 18px/22px "Open Sans",sans-serif;text-align:center}
.quals{left:22px;top:54px;font:700 10.5px "PT Sans",sans-serif;white-space:nowrap}
.about-text{left:22px;top:214px;width:214px;font-size:9.3px;line-height:12.2px;text-align:justify}
.interest{left:22px;top:346px;width:215px;color:var(--white);font-size:9.6px;line-height:12.4px}
.interest h3{color:#8fd3f4;font-size:10.6px;font-weight:400;margin-top:2px}
.interest ul{list-style:none;margin-top:10px}
.interest li{font-weight:700;font-size:9.4px;line-height:12px;margin-bottom:12.5px;padding-left:8px;text-indent:-8px}
.interest li::before{content:"● ";font-size:7px}

.contact{left:258px;top:11px;width:252px;height:580px}
.brand{left:30px;top:40px;width:200px;text-align:center;color:var(--navy);font:700 17px "PT Sans",sans-serif;letter-spacing:.5px}
.brand-sub{left:30px;top:62px;width:200px;text-align:center;color:#5a7ea8;font-size:5.8px;letter-spacing:1.2px}
.sect{color:var(--navy);font:700 14px "PT Sans",sans-serif}
.loc-head{left:27px;top:338px}
.touch-head{left:24px;top:449px}
.line{font-size:9.6px;line-height:12px}
.line svg{position:absolute;left:-17px;top:1px}
.l1{left:40px;top:366px}
.l2{left:40px;top:414px}
.c1{left:45px;top:486px}
.c2{left:45px;top:506px}
.c3{left:45px;top:526px}
.c4{left:45px;top:546px}

.cover{left:510px;top:11px;width:250px;height:580px}
.quote{left:40px;top:284px;color:var(--bright);font:700 46px/1 "Open Sans",sans-serif}
.t-my{left:88px;top:288px;font:400 26px/28px "Open Sans",sans-serif;color:#222}
.t-ankle{left:38px;top:340px;font:700 47px/50px "Open Sans",sans-serif;color:var(--bright)}
.t-sol{left:38px;top:390px;font:400 26px/28px "Open Sans",sans-serif;color:#222}
.t-sol span{background:var(--navy);color:var(--white);padding:0 4px}
.t-arth{left:42px;top:421px;font:400 24.5px/28px "Open Sans",sans-serif;color:#222}
.doc{left:37px;top:470px;font-size:12.6px;line-height:15.5px}
.doc span{background:var(--navy);color:var(--white);padding:0 2px}

/* inside */
.inside h2{position:absolute;left:0;width:100%;text-align:center;color:var(--white);font:italic 700 19.5px "Open Sans",sans-serif;white-space:nowrap}
.inside h2::after{content:"";display:block;margin:3px auto 0;width:170px;height:1px;background:rgba(255,255,255,.8)}
.copy{position:absolute;color:var(--white);font-size:8.4px;line-height:11px}
.copy p{margin-bottom:8px}
.dark-copy{position:absolute;font-size:8.6px;line-height:11.2px;text-align:justify;color:var(--ink)}
.dark-copy p{margin-bottom:9px}
.more{position:absolute;width:100%;text-align:center;font-size:8.6px;line-height:11px}
.visit{display:inline-block;background:var(--navy);color:var(--white);padding:0 5px;font-size:9.8px;line-height:13px;margin-top:4px}
.url{display:block;font-weight:700;font-size:9.8px;margin-top:2px}

.arthritis{left:10px;top:610px;width:248px;height:580px}
.fusion{left:258px;top:610px;width:252px;height:580px}
.replace{left:510px;top:610px;width:250px;height:580px}
.results{left:276px;top:1036px;width:484px;height:140px;background:var(--navy);border-radius:70px 0 0 70px;color:var(--white)}
.results h2{position:absolute;top:7px;left:0;width:100%;text-align:center;font:italic 700 17px "Open Sans",sans-serif}
.results h2::after{content:"";display:block;margin:2px auto 0;width:150px;height:1px;background:rgba(255,255,255,.8)}
.results p{position:absolute;left:28px;top:45px;width:436px;text-align:center;font-size:8.6px;line-height:11.4px}
</style>
</head>
<body>

<!-- Outside: about panel -->
<section class="panel about">
  <svg class="bg" width="248" height="580" viewBox="0 0 248 580">
    <defs>
      <linearGradient id="aboutBlue" x1="0" y1="0" x2="0" y2="1">
        <stop offset="0" stop-color="#0b63b8"/><stop offset="1" stop-color="#0a3f8f"/>
      </linearGradient>
    </defs>
    <path d="M0,262 C10,300 40,318 110,322 C180,326 225,328 248,345 V580 H0 Z" fill="url(#aboutBlue)"/>
    <circle cx="126" cy="137" r="66" fill="none" stroke="var(--sky)" stroke-width="3"/>
  </svg>
  <div class="abs name-bar">Dr Martin Hale</div>
  <div class="abs quals">MBBS (UEC), FRACS (Ortho), FA (Ortho</div>
  <div class="photo" role="img" aria-label="Portrait photo of the surgeon" style="left:64px;top:75px;width:124px;height:124px;border-radius:50%;background:radial-gradient(circle at 50% 40%,#d9dde2,#7a8592)"></div>
  <p class="abs about-text">Dr Martin Hale is an Australian trained Orthopaedic Surgeon who has a primary focus in the treatment of conditions of the foot and ankle. He has completed post fellowship training in Foot and Ankle surgery both locally and internationally, and continues to update himself in the latest techniques.</p>
  <div class="abs interest">
    <p>Dr Hale provides assessment and treatment of all foot and ankle conditions.</p>
    <h3>He has special interest in the following:</h3>
    <ul>
      <li>Minimally invasive treatment for bunions and toe deformities.</li>
      <li>Joint sparing procedures for arthritis or deformity, including the Flexa implant.</li>
      <li>Joint fusion procedures for arthritis of the feet and ankle.</li>
      <li>Sports injuries and tendinopathies.</li>
      <li>Total ankle replacement and deformity correction of the foot and ankle.</li>
    </ul>
  </div>
</section>

<!-- Outside: contact panel -->
<section class="panel contact">
  <svg class="bg" width="252" height="580" viewBox="0 0 252 580">
    <path d="M14,214 A112,112 0 0 0 238,214 A112,118 0 0 1 14,214 Z" fill="var(--navy)" transform="translate(0,6)"/>
  </svg>
  <div class="abs brand">HOLLOWBROOK CLINIC</div>
  <div class="abs brand-sub">MEDICAL &amp; SURGICAL SPECIALISTS</div>
  <div class="photo" role="img" aria-label="Photo of the modern clinic building against a blue sky" style="left:16px;top:103px;width:220px;height:220px;border-radius:50%;background:linear-gradient(160deg,#3a8ed8,#9cc7ec 55%,#dfe7ee)"></div>
  <h3 class="abs sect loc-head">Locations :</h3>
  <div class="abs line l1"><svg width="12" height="12" viewBox="0 0 12 12"><circle cx="6" cy="6" r="5.5" fill="var(--navy)"/><circle cx="6" cy="5" r="2" fill="#fff"/></svg>Suite 701-701, Level 7<br>Harbourside Private Hospital<br>212-216 Kellet St&nbsp;&nbsp; Brightwater NSW</div>
  <div class="abs line l2"><svg width="12" height="12" viewBox="0 0 12 12"><circle cx="6" cy="6" r="5.5" fill="var(--navy)"/><circle cx="6" cy="5" r="2" fill="#fff"/></svg>48 River Road&nbsp;&nbsp; Eastmere NSW</div>
  <h3 class="abs sect touch-head">Get in Touch :</h3>
  <div class="abs line c1"><svg width="12" height="12" viewBox="0 0 12 12"><circle cx="6" cy="6" r="6" fill="var(--navy)"/><path d="M3.5,4 h5 v4.5 h-5z" fill="#fff"/></svg>(02) 5550 1234</div>
  <div class="abs line c2"><svg width="12" height="12" viewBox="0 0 12 12"><circle cx="6" cy="6" r="6" fill="var(--navy)"/><path d="M3.2,4.5 h5.6 v3.5 h-5.6z M4.2,3 h3.6 v1.5 h-3.6z" fill="#fff"/></svg>(02) 5550 5678</div>
  <div class="abs line c3"><svg width="12" height="12" viewBox="0 0 12 12"><circle cx="6" cy="6" r="6" fill="var(--navy)"/><path d="M3,4 h6 v4 h-6z" fill="#fff"/><path d="M3,4 l3,2.2 l3,-2.2" stroke="var(--navy)" stroke-width=".8" fill="none"/></svg>info@hollowbrookclinic.com.au</div>
  <div class="abs line c4"><svg width="12" height="12" viewBox="0 0 12 12"><circle cx="6" cy="6" r="6" fill="var(--navy)"/><circle cx="6" cy="6" r="3.3" fill="none" stroke="#fff" stroke-width=".8"/><path d="M2.7,6 h6.6 M6,2.7 v6.6" stroke="#fff" stroke-width=".7"/></svg>www.hollowbrookclinic.com.au</div>
</section>

<!-- Outside: cover -->
<section class="panel cover">
  <div class="photo" role="img" aria-label="Photo of a runner holding a painful ankle on a sunny trail" style="left:0;top:0;width:250px;height:340px;background:linear-gradient(170deg,#d8c9a6,#b9a36e 45%,#8e7b45)"></div>
  <svg class="bg" width="250" height="580" viewBox="0 0 250 580">
    <path d="M0,330 C10,270 70,230 150,230 C210,230 240,210 250,190 V580 H0 Z" fill="#fff"/>
    <path d="M0,330 C10,270 70,230 150,230 C210,230 240,210 250,190 V200 C235,222 205,240 150,240 C75,240 12,280 0,340 Z" fill="var(--navy)"/>
    <path d="M250,460 C240,520 170,545 80,550 C40,552 10,565 0,580 H250 Z" fill="var(--navy)"/>
    <path d="M250,470 C238,525 170,550 85,556 C45,560 15,572 8,580 H0 C10,565 40,552 80,550 C170,545 240,520 250,460 Z" fill="var(--sky)"/>
  </svg>
  <div class="abs quote">“</div>
  <div class="abs t-my">MY<br>PAINFUL</div>
  <div class="abs t-ankle">ANKLE</div>
  <div class="abs t-sol"><span>Solutions</span> for</div>
  <div class="abs t-arth">Ankle Arthritis</div>
  <div class="abs doc"><span>Dr Martin Hale</span><br>Orthopaedic Foot and<br>Ankle Surgeon</div>
</section>

<!-- Inside: ankle arthritis -->
<section class="panel inside arthritis">
  <svg class="bg" width="248" height="580" viewBox="0 0 248 580">
    <defs>
      <linearGradient id="skyBlob" x1="0" y1="0" x2="0" y2="1">
        <stop offset="0" stop-color="#1d8fd2"/><stop offset="1" stop-color="#0a63b6"/>
      </linearGradient>
    </defs>
    <path d="M0,0 H248 V215 C248,300 195,340 124,340 C53,340 0,300 0,215 Z" fill="url(#skyBlob)"/>
    <path d="M0,520 C20,560 60,575 110,580 H0 Z" fill="var(--navy)"/>
  </svg>
  <h2 style="top:28px">Ankle arthritis</h2>
  <div class="copy" style="left:16px;top:64px;width:216px;text-align:center">
    <p>Ankle arthritis is a painful condition where there is loss of cartilage from the ankle joint surface. Although not as common as knee or hip arthritis, pain can be debilitating affecting quality of life.</p>
    <p>Arthritis of the joint can be caused by trauma joint such as fracture or recurrent instability or secondary from inflammatory conditions such as rheumatoid arthritis.</p>
    <p>Pain from the joint will occur with activity causing a limp, limiting walking speed and distance. Often there is swelling of the joint with progressive loss of motion.</p>
    <p>Diagnosis is made with examination of the ankle and weight bearing x-rays showing loss of joint</p>
  </div>
  <div class="photo" role="img" aria-label="X-ray of an arthritic ankle joint" style="left:66px;top:228px;width:116px;height:116px;border-radius:50%;border:3px solid #fff;background:radial-gradient(circle at 45% 45%,#cfcfcf,#4a4a4a 60%,#111)"></div>
  <div class="dark-copy" style="left:22px;top:366px;width:214px">
    <p>When pain medication, activity modification and shoe ware modification is no longer effective to control the pain then then it is worthwhile discussing with your GP for referral to Dr Martin Hale for an opinion on further treatment. As an Orthopaedic Foot and Ankle surgeon, he will be able to assess your conditions and give advice on the best options for your treatment.</p>
    <p>The decision on the best option is based on your age, activity level, existing medical problems, previous ankle treatment and your expected outcome from treatment. In the situation of end stage arthritis options consist of either Ankle fusion or Total Ankle replacement.</p>
  </div>
</section>

<!-- Inside: ankle fusion -->
<section class="panel inside fusion">
  <svg class="bg" width="252" height="580" viewBox="0 0 252 580">
    <defs>
      <linearGradient id="navyBlob" x1="0" y1="0" x2="0" y2="1">
        <stop offset="0" stop-color="#0b5cb0"/><stop offset="1" stop-color="#073f8c"/>
      </linearGradient>
    </defs>
    <path d="M0,0 H252 V150 C252,255 200,300 126,300 C52,300 0,255 0,150 Z" fill="url(#navyBlob)"/>
  </svg>
  <h2 style="top:28px">Ankle Fusion Surgery</h2>
  <div class="copy" style="left:14px;top:66px;width:224px;text-align:center">
    <p>This operation aims to stiffen the ankle joint by fusing the tibia and talus together in the optimal position for function. The common thought is that there will be no movement of the foot, and the patient will walk with a limp. The fusion only occurs at the ankle joint, leaving motion available to the surrounding joints. Although there is decreased motion, you will walk more normally after a fusion without a limp as the pain to the joint is removed.</p>
  </div>
  <div class="photo" role="img" aria-label="X-ray of an ankle fused with plates and screws" style="left:68px;top:192px;width:116px;height:116px;border-radius:50%;border:3px solid #fff;background:radial-gradient(circle at 50% 45%,#e2e2e2,#5a5a5a 55%,#111)"></div>
  <div class="more" style="top:322px">For more information on<br>ankle fusion, risks and recovery<br><span class="visit">Visit our website :</span><span class="url">www.hollowbrookclinic.com.au/Ankle-Fusion</span></div>
</section>

<!-- Inside: total ankle replacement -->
<section class="panel inside replace">
  <svg class="bg" width="250" height="580" viewBox="0 0 250 580">
    <path d="M0,0 H250 V240 C250,290 225,290 205,285 C195,330 160,350 118,350 C70,350 40,325 32,290 C15,290 0,280 0,260 Z" fill="#1b8fd0"/>
  </svg>
  <h2 style="top:30px;font-size:15px">Total Ankle Replacement Surgery</h2>
  <div class="copy" style="left:12px;top:66px;width:226px;text-align:justify">
    <p>In suitable patients there may be the option to maintain joint motion and perform a Total Ankle Replacement. Like a hip or knee replacement operation, the arthritic joint is removed and replaced with an artificial joint. Like an ankle fusion there will alleviation of the pain and limp with maintenance of the ankle joint motion. Recovery to walking post-surgery is often much sooner than with ankle fusion. Dr Martin Hale is one of the few surgeons to have completed an international fellowship in ankle replacement surgery and has been performing the technique since 2008. He is currently performing the technique using the Meridian Total ankle with Guidepoint guides.</p>
  </div>
  <div class="photo" role="img" aria-label="X-ray of an ankle with a total joint replacement implant" style="left:62px;top:230px;width:116px;height:116px;border-radius:50%;border:3px solid #fff;background:radial-gradient(circle at 50% 40%,#f0f0f0,#5e5e5e 50%,#111)"></div>
  <div class="more" style="top:360px">For more information on<br>ankle fusion, risks and recovery<br><span class="visit">Visit our website :</span><span class="url">www.hollowbrookclinic.com.au/Ankle-Replacement</span></div>
</section>

<!-- Inside: results band -->
<section class="panel results">
  <h2>Results of surgery</h2>
  <p>Successful surgery in the suitable patient will help resolve the pain associated with the ankle arthritis. Ankle Fusion surgery is ideal for patients with heavy labour work, allowing them to return to previous activities. There may be the risk of arthritis to surrounding joints in the future, but often this occurs many years down the track. Results from Total Ankle replacement surgery have been improving over the years, but there is known risks of loosening, cyst formation or failure of the joint over time that can occur in some patients. It is important to have a opinion from an Orthopaedic Foot and Ankle Surgeon experienced in the these procedure to determine which procedure will provide the best long term solution for you.</p>
</section>

</body>
</html>
```